Stationery Design Project

We need a stationery design to change our look to a more corporate design. My company has been established since 1989 and over that time has changed from your average sign company to doing more Corporate re branding projects and have some multi National clients.
Our website is currently being redesigned so we need a new logo and business cards etc. to compliment it.
I have 2 graphic designers employed but i want on outsiders opinion and a totally independant view point.
Updates
Hi Designers
We are predominantely a sign manufacturing company that manufacturers every type of sign you can imagine. However the majoprity of our work is digital graphics. Our claim to faim is that we wrap the Harbourtown Skytrams and Cityglides which everyone seems to know in Sydney.We also do all sorts of Large format digital printing, vehicle wraps,vinyl signage,LED & Neon Illuminated signage,CNC Routing all materials,Laser cutting and Engraving, Architectural signage, Cut Out letters and Screenprinting.
Aswell as this we totally re-brand companies with internal wall graphics reception signage way finding signage and the like.We are a medium size company that has been trading since 1989 and has some very large reputable clients.
Our Company name is Brackwell Pty Ltd but like to have Signage and Graphics in our stationery.
Our details are as follows T: 9381 5027 F: 9381 5093 Unit 4, 22 Tallowood Lane.Kenbury Flats. NSW 2163 email mail@brackwellsigns.example our current website is being re-designed www.brackwellsigns.example
The design and colour scheme i would like is quite simple with a corporate feel and blue, grey & magenta are colours that seem to suit but am open to most suggestions just looking for clean lines.
Hopefully this is enough information if you require any more please ask.
Regards Dennis Albrook
Reason: I did not supply much information at first
Reason: I have extended it due to Christmas holidays
We are looking to simplify our LOGO not too concerned yet about layout of stationery items that we can easily work on later. I want to get a new logo that we can work with before we return to work on the 16th January so please concentrate on just the logo for now.
We would like to have Signs & Graphics somewhere in the name even though our registered name is Brackwell Pty Ltd. Brackwell is one word, i want it to be quite a bold font with no seriffs.The bright blue and grey colours are favourites so far with maybe a little magenta added later. Would like to have a Logo that is totally seperate and then the Brackwell P/L Signs & graphics as a secondary item just to let people know what Brackwell do as the name obviously does not say what we are about.
Also we need to consider how we can put logo on T-shirts work shirts and company vehicles.
We do not need CD cover or envelopes but letterheads and business cards.
Reason: I want everyone to concentrate on a logo we return to work on the 16th of January so would like to have at least a logo approved by then
Reason: We are close to making a decision and just need a few more days for a couple of designers to submit extra things we have asked of them.
Business

```html
<!DOCTYPE html>
<html lang="en">
<head>
<meta charset="utf-8">
<title>Brackwell business cards</title>
<link rel="stylesheet" href="https://fonts.googleapis.com/css2?family=Source+Sans+3:wght@300;400;600&display=swap">
<style>
  :root {
    --stage: #e9e9e9;
    --card-grey: #666666;
    --ring-grey: #636363;
    --white: #ffffff;
    --ink: #1a1a1a;
    --text: #333333;
    --muted: #6a6a6a;
    --teal: #0a86b3;
    --magenta: #ec0c84;
    --pink-soft: #f45aa8;
    --blue: #1592bf;
    --blue-light: #5fc3dc;
  }
  html, body {
    margin: 0;
    width: 1200px;
    height: 960px;
    overflow: hidden;
    background: radial-gradient(ellipse at center, #fbfbfb 0%, var(--stage) 70%);
    font-family: "Source Sans 3", "Helvetica Neue", Arial, sans-serif;
  }
  .card {
    position: absolute;
    width: 634px;
    height: 364px;
    border-radius: 18px;
    overflow: hidden;
  }
  .card-front { left: 246px; top: 95px; background: var(--card-grey); }
  .card-back  { left: 255px; top: 482px; background: linear-gradient(180deg, #ffffff 55%, #ececec 100%); }
  .card svg.art { position: absolute; inset: 0; }
  .brand {
    position: absolute;
    display: flex;
    align-items: center;
    gap: 14px;
  }
  .brand-dot { border-radius: 50%; flex: none; }
  .brand-name { font-weight: 400; letter-spacing: 0.5px; line-height: 1; }
  .card-front .brand { left: 304px; top: 266px; }
  .card-front .brand-dot { width: 66px; height: 66px; background: var(--blue); }
  .card-front .brand-name { font-size: 44px; color: var(--white); }
  .card-back .brand { left: 28px; top: 26px; }
  .card-back .brand-dot { width: 80px; height: 80px; background: var(--blue); }
  .card-back .brand-name { font-size: 44px; color: var(--ink); }
  .contact {
    position: absolute;
    left: 36px;
    top: 140px;
    color: var(--text);
    font-weight: 300;
    font-size: 16px;
    line-height: 21px;
  }
  .person-name { color: var(--teal); font-weight: 600; font-size: 24px; line-height: 28px; margin: 0; }
  .person-role { color: var(--muted); font-size: 16px; margin: 0 0 20px; }
  .address { margin: 0 0 6px; }
  .lines { list-style: none; margin: 0; padding: 0; }
  .lines li { display: flex; align-items: center; gap: 12px; height: 22.5px; }
  .lines svg { width: 16px; height: 14px; flex: none; }
</style>
</head>
<body>

<section class="card card-front" aria-label="Business card front">
  <svg class="art" width="634" height="364" viewBox="0 0 634 364">
    <defs>
      <linearGradient id="markFront" x1="0" y1="0" x2="1" y2="1">
        <stop offset="0" stop-color="var(--magenta)"/>
        <stop offset="0.45" stop-color="var(--blue-light)"/>
        <stop offset="1" stop-color="#0a82af"/>
      </linearGradient>
    </defs>
    <circle cx="82" cy="175" r="205" fill="var(--white)"/>
    <circle cx="82" cy="175" r="184" fill="var(--ring-grey)"/>
    <circle cx="82" cy="175" r="166" fill="url(#markFront)" role="img" aria-label="Large brand mark decoration area"/>
  </svg>
  <div class="brand">
    <span class="brand-dot"></span>
    <span class="brand-name">Brackwell</span>
  </div>
</section>

<section class="card card-back" aria-label="Business card back">
  <svg class="art" width="634" height="364" viewBox="0 0 634 364">
    <defs>
      <linearGradient id="markBack" x1="0" y1="0" x2="1" y2="1">
        <stop offset="0" stop-color="var(--pink-soft)"/>
        <stop offset="0.5" stop-color="#fbe3ef"/>
        <stop offset="0.55" stop-color="var(--blue-light)"/>
        <stop offset="1" stop-color="#0a82af"/>
      </linearGradient>
    </defs>
    <circle cx="529" cy="216" r="213" fill="var(--ring-grey)"/>
    <circle cx="529" cy="216" r="190" fill="var(--white)"/>
    <circle cx="529" cy="216" r="174" fill="url(#markBack)" role="img" aria-label="Large brand mark decoration area"/>
  </svg>

  <div class="brand">
    <span class="brand-dot"></span>
    <span class="brand-name">Brackwell</span>
  </div>

  <div class="contact">
    <p class="person-name">Warren Halloway</p>
    <p class="person-role">Marketing Manager</p>
    <p class="address">22 Tallowood Lane<br>Kenbury Flats. NSW 2163</p>
    <ul class="lines">
      <li>
        <svg viewBox="0 0 16 14" aria-label="Phone"><path d="M1 5c0-3 14-3 14 0v1.5h-3.5V5h-7v1.5H1z M4 7h8l2 6H2z" fill="var(--teal)"/></svg>
        9381 5027
      </li>
      <li>
        <svg viewBox="0 0 16 14" aria-label="Fax"><rect x="4" y="1" width="8" height="4" fill="none" stroke="var(--teal)" stroke-width="1.2"/><rect x="2" y="5" width="12" height="6" fill="none" stroke="var(--teal)" stroke-width="1.2"/><rect x="4" y="9" width="8" height="4" fill="none" stroke="var(--teal)" stroke-width="1.2"/></svg>
        9381 5093 Unit 4
      </li>
      <li>
        <svg viewBox="0 0 16 14" aria-label="Email"><rect x="1" y="2" width="14" height="10" fill="none" stroke="var(--teal)" stroke-width="1.4"/><path d="M1 2l7 6 7-6" fill="none" stroke="var(--teal)" stroke-width="1.4"/></svg>
        warren@brackwellsigns.example
      </li>
      <li>
        <svg viewBox="0 0 16 14" aria-label="Website"><circle cx="8" cy="7" r="6" fill="none" stroke="var(--teal)" stroke-width="1.2"/><ellipse cx="8" cy="7" rx="2.6" ry="6" fill="none" stroke="var(--teal)" stroke-width="1"/><path d="M2 7h12" stroke="var(--teal)" stroke-width="1"/></svg>
        www.brackwellsigns.example
      </li>
    </ul>
  </div>
</section>

</body>
</html>
```